Velmora Outcomes Brochure Design Project

- Who we are?
Velmora Outcomes is New Internet Marketing Company Based in China.

It is our aim to provide Chinese clients with the means to internationally market their product, via the Internet.

Our primary products are Outsourced Design ( Thanks to Pixel hive and the amazing designers who use it), SEO and Virtual Hosting.

- Project Brief
Design a vibrant and fresh brochure that introduces the fundamentals of SEO. There is no restriction to the number of pages, however all the info I have included in this brief must be included.

- Colour Palette
Please see link or download the Adobe Swatch Exchange File or follow the link below
http://tintaro.example.com/#themes/search?term=5830716
Updates

Logo updated - grey background removed

Various file formats added for logo and brochure content

Brochure zip file add containing logo in different formats.

Adobe color scheme file added

The general corporate colors are:

Base Color: CMYK :0, 60, 80, 0  Hex: FF6633
Dark Orange: CMYK: 0, 72, 96, 30 Hex: B23308
Light Orange: CMYK 0, 42, 56, 0 Hex: FF9571
Grey: CMYK 0, 0, 0, 48 Hex: 858585
Light Grey: CMYK 0, 0, 0, 26 Hex: BDBDBD

Please note that I'm happy for other colors to be included, however I would like these the corporate branding colors to be clearly present through the brochure.

Hi All

First place payment has increased to $600 - Looking to see some creative designs!

Hi All

Project Deadline Extended
Reason: I have increase the budget and extend the deadline as I need to see more design.

I have attached a zip file that contains example brochures I like.

We are not keen on the table data its a little plain. We have create an info-graphic to replace one of the table and would like to see it included in the design.

Project Deadline Extended
Reason: A few designers have asked for this extension and I would like to see additional designs. Thanks Marek

Target Market(s)

- Our Target Audience is..
It is small to medium businesses looking to reach out to the international market.
Our clients still very much operate on a face to face level in business and are new to the concept of Internet marketing

However this must look professional, Marketable and Clean, with the power of connecting people globally, through SEO and design to be reflected visually in the brochure.

Industry/Entity Type

Internet

Requirements
Must have
• One or more of the FACTS that I have highlighted need to stand out on each page. These FACTS can be found the document attached to this brief and are under the section titled 'Did You Know!'. Not every fact in this section needs to be highlighted in the brochure, but each page needs to have at least, one or more fact that stands out, soemwhere on the page.
See attached document, under the heading 'Did you Know!' and use one or two of these facts to spruce up the pages!

One image/ per page or per two pages MUST be included!

- Provide stock photos and please send us a message with the additional cost of these with your submission

The Table data, that I have included in the attachment must be included in the body of the pages - BUT the table format is not necessary and you can place the information in the body like plain text.

The brochure size should be a little larger than A4.

Please design the back page, like a pocket to hold paper and other material in it that I include with this brochure.

```html
<!DOCTYPE html>
<html lang="en">
<head>
<meta charset="utf-8">
<title>Velmora Outcomes — Packages, Pages 13–14</title>
<link href="https://fonts.googleapis.com/css2?family=Exo+2:wght@500;700&family=Lato:wght@400;700&display=swap" rel="stylesheet">
<style>
:root{
  --backdrop:#e4e6e6;
  --paper:#ffffff;
  --orange:#f2643a;
  --label-grey:#9b9d9c;
  --value-grey:#cfd6d2;
  --rule:#9a9a9a;
  --ink:#1e1e1e;
  --night:#141c28;
  --night-mid:#26344a;
  --headline-grey:#c9ced4;
  --folio:#c8c8c8;
}
*{box-sizing:border-box;margin:0;padding:0}
html,body{width:1200px;height:900px;overflow:hidden;background:var(--backdrop)}
body{font-family:"Lato",sans-serif;color:var(--ink);position:relative}
.spread{position:absolute;left:38px;top:57px;width:1127px;height:788px;background:var(--paper)}
.fold{position:absolute;left:563px;top:0;height:100%;border-left:1px dashed #8c8c8c}
.block{position:absolute}
.tag{display:inline-block;background:var(--orange);color:#fff;font-size:13px;letter-spacing:.2px;
  height:23px;line-height:23px;padding:0 8px;margin-bottom:6px;text-transform:uppercase;white-space:nowrap}
.tags{display:flex;flex-direction:column;align-items:flex-start}
.intro{font-size:8.6px;line-height:12.8px;width:152px;margin-top:6px}
.rule{position:absolute;height:0;border-top:2px solid var(--rule)}
.specs{position:absolute;width:312px}
.spec-group{display:grid;grid-template-columns:155px 154px;column-gap:3px;row-gap:3px;margin-bottom:13px}
.spec-label,.spec-value{height:14px;line-height:14px;font-size:9px}
.spec-label{background:var(--label-grey);color:#fff;padding-left:4px}
.spec-value{background:var(--value-grey);text-align:center}
.note{position:absolute;font-size:8.6px;line-height:12.8px;width:320px}
.hero{position:absolute;left:565px;top:0;width:562px;height:383px;
  background:radial-gradient(ellipse at 75% 45%,var(--night-mid) 0%,var(--night) 60%,#0c111a 100%)}
.hero-art{position:absolute;inset:0}
.fact{position:absolute;left:19px;top:100px;border-left:5px solid #fff;padding-left:13px;
  font-family:"Exo 2",sans-serif;font-weight:500;color:var(--headline-grey);font-size:23px;line-height:27px}
.fact-number{display:block;font-weight:700;color:#fff;font-size:60px;line-height:56px;margin:2px 0 0}
.folio{position:absolute;left:1083px;top:749px;font-size:9px;color:var(--folio)}
</style>
</head>
<body>
<main class="spread">
  <!-- Left page -->
  <section class="package">
    <div class="block tags" style="left:39px;top:103px">
      <span class="tag">Start-up Bronze</span><span class="tag">Package</span>
      <p class="intro">Just starting up and don't have a bank full of capital? Don't panic - our Start-up package is for you. We will help optimize your website and online marketing strategy, and get those much needed customers spending their money with you.</p>
    </div>
    <div class="specs" style="left:210px;top:102px">
      <div class="spec-group">
        <div class="spec-label">Website Size</div><div class="spec-value">10 pages</div>
        <div class="spec-label">No. of Keywords</div><div class="spec-value">5</div>
        <div class="spec-label">Keywords on the first page</div><div class="spec-value">3</div>
        <div class="spec-label">Delivery time frame</div><div class="spec-value">3 to 6 months</div>
      </div>
      <div class="spec-group">
        <div class="spec-label">Manual Directory Submission</div><div class="spec-value">200</div>
        <div class="spec-label">Article Submission</div><div class="spec-value">50</div>
        <div class="spec-label">Forum Posting</div><div class="spec-value">20</div>
        <div class="spec-label">Blog Commenting</div><div class="spec-value">10</div>
        <div class="spec-label">Blog Creation</div><div class="spec-value">Yes</div>
        <div class="spec-label">Social Bookmarking Submission</div><div class="spec-value">50</div>
      </div>
    </div>
  </section>
  <div class="rule" style="left:39px;top:292px;width:486px"></div>

  <section class="package">
    <div class="block tags" style="left:39px;top:305px">
      <span class="tag">Small Business</span><span class="tag">Silver Package</span>
      <p class="intro">Do you have an established small business and are looking to reach more consumers and a wider market. Let our expects do the hard work for you and watch you international contacts grow.</p>
    </div>
    <div class="specs" style="left:210px;top:305px">
      <div class="spec-group">
        <div class="spec-label">Website Size</div><div class="spec-value">20 pages</div>
        <div class="spec-label">No. of Keywords</div><div class="spec-value">10</div>
        <div class="spec-label">Keywords on the first page</div><div class="spec-value">6</div>
        <div class="spec-label">Delivery time frame</div><div class="spec-value">3 to 6 months</div>
      </div>
      <div class="spec-group">
        <div class="spec-label">Manual Directory Submission</div><div class="spec-value">400</div>
        <div class="spec-label">Article Submission</div><div class="spec-value">75</div>
        <div class="spec-label">Forum Posting</div><div class="spec-value">40</div>
        <div class="spec-label">Blog Commenting</div><div class="spec-value">15</div>
        <div class="spec-label">Blog Creation</div><div class="spec-value">Yes</div>
        <div class="spec-label">Social Bookmarking Submission</div><div class="spec-value">100</div>
      </div>
    </div>
  </section>
  <div class="rule" style="left:39px;top:499px;width:486px"></div>

  <section class="package">
    <div class="block tags" style="left:39px;top:512px">
      <span class="tag">Medium Business</span><span class="tag">Gold Package</span>
      <p class="intro">Got a well established client base? Looking to improve you annual turnover or simply looking to increase profits and reduce your overheads? Internet marketing is the best choice to boost you sales.</p>
    </div>
    <div class="specs" style="left:210px;top:513px">
      <div class="spec-group">
        <div class="spec-label">Website Size</div><div class="spec-value">40 pages</div>
        <div class="spec-label">No. of Keywords</div><div class="spec-value">20</div>
        <div class="spec-label">Keywords on the first page</div><div class="spec-value">12</div>
        <div class="spec-label">Delivery time frame</div><div class="spec-value">6 months</div>
      </div>
      <div class="spec-group">
        <div class="spec-label">Manual Directory Submission</div><div class="spec-value">600</div>
        <div class="spec-label">Article Submission</div><div class="spec-value">100</div>
        <div class="spec-label">Forum Posting</div><div class="spec-value">60</div>
        <div class="spec-label">Blog Commenting</div><div class="spec-value">20</div>
        <div class="spec-label">Blog Creation</div><div class="spec-value">Yes</div>
        <div class="spec-label">Social Bookmarking Submission</div><div class="spec-value">150</div>
      </div>
    </div>
    <p class="note" style="left:207px;top:701px">Included in both the gold package and above is Social Media Marketing. Contact us for more details.</p>
  </section>

  <div class="fold"></div>

  <!-- Right page -->
  <div class="hero">
    <div class="hero-art" role="img" aria-label="Photo of a businessman sketching connected laptops linked to a central network node"></div>
    <p class="fact">There<br>are over<span class="fact-number">110</span>billion global<br>searches being<br>conducted<br>each month.</p>
  </div>

  <div class="rule" style="left:602px;top:410px;width:487px"></div>
  <section class="package">
    <div class="block tags" style="left:602px;top:422px">
      <span class="tag">Large Business</span><span class="tag">Diamond Package</span>
      <p class="intro">Are you already a large international company looking to further improve you international and domestic market position? Our experts can drive down your overheads and drive your profits up.</p>
    </div>
    <div class="specs" style="left:774px;top:422px">
      <div class="spec-group">
        <div class="spec-label">Website Size</div><div class="spec-value">80 pages</div>
        <div class="spec-label">No. of Keywords</div><div class="spec-value">40</div>
        <div class="spec-label">Keywords on the first page</div><div class="spec-value">24</div>
        <div class="spec-label">Delivery time frame</div><div class="spec-value">6 months</div>
      </div>
      <div class="spec-group">
        <div class="spec-label">Manual Directory Submission</div><div class="spec-value">800</div>
        <div class="spec-label">Article Submission</div><div class="spec-value">125</div>
        <div class="spec-label">Forum Posting</div><div class="spec-value">80</div>
        <div class="spec-label">Blog Commenting</div><div class="spec-value">80</div>
        <div class="spec-label">Blog Creation</div><div class="spec-value">Yes</div>
        <div class="spec-label">Social Bookmarking Submission</div><div class="spec-value">200</div>
      </div>
    </div>
    <p class="note" style="left:771px;top:611px">Included in both the gold package and above is Social Media Marketing. Contact us for more details..</p>
  </section>

  <span class="folio">14</span>
</main>
</body>
</html>
```